Innovative Healthcare Technology Company needs a Business Card Design

We are in need of an innovative business card design for a new healthcare software company called "Brightwell Harbor Systems". We develop software that creates medical assessment applications and mobile e-learning prevention services to reduce risk behaviors in adolescent and young adults. Our initial product, the "MERIDIAN App", conducts a tailored sexual risk assessment and provides a doctor with an insightful patient report to improve sexual risk counseling and ultimately reduce unintended pregnancy, STDs, etc.

We would like the design to incorporate our logo and branding colors (attached) in an innovative and creative manner. The final design should communicate professionalism and healthcare innovation. Our tag line is "prevention is the solution" (doesn't necessarily need to be included) and our target audience is doctors, medical directors, and medical business administrators. Please visit our website for additional info ourlantrixhub.com. Be creative and we look forward to seeing your designs!

Target Market(s)

healthcare - doctors, medical directors and medical business administrators

Industry/Entity Type

Healthcare

Contact Information for Business Card

We would like the design to incorporate our logo and branding colors (attached) in an innovative and creative manner. The final design should communicate professionalism and healthcare innovation. Our tag line is "prevention is the solution" (doesn't necessarily need to be included)

Font styles to use
Other font styles liked:
• quicksand

Requirements
Must have
• our logo and brand colors
• Name, (Joan Ferraventi, PhD)
• Email (drjoan@ourlantrixhub.com)
• phone (555.213.8870)
• Website (ourlantrixhub.com)
Should not have
• cartoon look

```html
<!DOCTYPE html>
<html lang="en">
<head>
<meta charset="utf-8">
<title>Brightwell Harbor Systems – Business Card</title>
<link rel="stylesheet" href="https://fonts.googleapis.com/css2?family=Quicksand:wght@500;600&family=Open+Sans:wght@400;600&display=swap">
<style>
  :root {
    --bg: #ececec;
    --paper: #ffffff;
    --navy: #1c4f8c;
    --navy-deep: #0e3668;
    --blue-light: #4a86bf;
    --ink: #22466f;
    --line: #3d6898;
    --muted: #5b6b7d;
    --pulse-soft: #dfe8f2;
    --shadow: rgba(20, 40, 70, 0.18);
  }
  * { margin: 0; padding: 0; box-sizing: border-box; }
  html, body { width: 1200px; height: 913px; overflow: hidden; background: var(--bg); }
  .canvas {
    width: 1200px; height: 913px;
    display: flex; flex-direction: column; align-items: center; justify-content: center;
    gap: 40px;
  }
  .card {
    position: relative;
    width: 700px; height: 400px;
    border-radius: 22px;
    overflow: hidden;
    box-shadow: 0 10px 30px var(--shadow);
  }

  /* ---------- Shared brand lockup ---------- */
  .brand {
    position: absolute; display: flex; align-items: center; gap: 12px;
    font-family: "Quicksand", sans-serif; font-weight: 600;
    white-space: nowrap;
  }
  .brand-mark { flex: none; }

  /* ---------- Front ---------- */
  .card-front { background: var(--paper); }
  .card-front .side-band {
    position: absolute; left: 36px; top: 0; bottom: 0; width: 42px;
    background: linear-gradient(180deg, var(--blue-light), var(--navy) 45%, var(--navy-deep));
  }
  .card-front .brand { left: 124px; top: 94px; font-size: 30px; color: var(--navy); }
  .card-front .brand-mark { width: 22px; height: 22px; background: var(--navy); }

  .pulse-area {
    position: absolute; right: 0; top: 150px; width: 150px; height: 58px;
    background: linear-gradient(90deg, rgba(223,232,242,0) 0%, var(--pulse-soft) 40%, var(--pulse-soft) 100%);
  }

  .person {
    position: absolute; left: 124px; right: 0; top: 188px;
    font-family: "Open Sans", sans-serif; color: var(--navy);
  }
  .person-row { display: flex; align-items: flex-end; gap: 16px; }
  .person-name { font-size: 24px; font-weight: 400; line-height: 1.2; white-space: nowrap; }
  .person-rule { flex: 1; height: 0; border-top: 1.3px solid var(--line); margin-bottom: 8px; }
  .person-title { font-size: 13px; color: var(--muted); margin-top: 2px; }

  .contact {
    position: absolute; left: 124px; top: 282px;
    list-style: none;
    font-family: "Open Sans", sans-serif; font-size: 15px; color: var(--ink);
  }
  .contact li { display: flex; align-items: center; gap: 10px; height: 24px; }
  .contact svg { width: 13px; height: 13px; flex: none; }
  .contact .web { font-weight: 600; }

  /* ---------- Back ---------- */
  .card-back {
    background: linear-gradient(150deg, #4f8cc4 0%, var(--navy) 45%, var(--navy-deep) 100%);
  }
  .card-back .side-band {
    position: absolute; left: 560px; top: 0; bottom: 0; width: 60px;
    background: var(--paper);
  }
  .card-back .cross { position: absolute; left: 500px; top: 40px; width: 120px; height: 120px; }
  .card-back .brand { left: 96px; top: 190px; font-size: 32px; color: var(--paper); }
  .card-back .brand-mark { width: 26px; height: 26px; background: var(--paper); }
</style>
</head>
<body>
<main class="canvas">

  <section class="card card-front" aria-label="Business card front">
    <div class="side-band"></div>
    <div class="brand"><span class="brand-mark"></span>Brightwell Harbor Systems</div>

    <div class="pulse-area" role="img" aria-label="Heartbeat pulse graphic"></div>

    <div class="person">
      <div class="person-row">
        <div class="person-name">Joan Ferraventi</div>
        <span class="person-rule"></span>
      </div>
      <div class="person-title">PhD</div>
    </div>

    <ul class="contact">
      <li>
        <svg viewBox="0 0 16 16" aria-hidden="true"><path fill="#5b6b7d" d="M4 1l3 3-2 2c1 2 3 4 5 5l2-2 3 3-2 3C7 15 1 9 1 3z"/></svg>
        (555.213.8870)
      </li>
      <li>
        <svg viewBox="0 0 16 16" aria-hidden="true"><rect x="1" y="3" width="14" height="10" fill="none" stroke="#5b6b7d" stroke-width="1.5"/><polyline points="1,3 8,9 15,3" fill="none" stroke="#5b6b7d" stroke-width="1.5"/></svg>
        drjoan@ourlantrixhub.com
      </li>
      <li class="web">
        <svg viewBox="0 0 16 16" aria-hidden="true"><circle cx="8" cy="8" r="6.5" fill="none" stroke="#5b6b7d" stroke-width="1.5"/><path d="M1.5 8h13M8 1.5c-3 3-3 10 0 13M8 1.5c3 3 3 10 0 13" fill="none" stroke="#5b6b7d" stroke-width="1.2"/></svg>
        www.ourlantrixhub.com
      </li>
    </ul>
  </section>

  <section class="card card-back" aria-label="Business card back">
    <div class="side-band"></div>
    <svg class="cross" viewBox="0 0 120 120" aria-hidden="true">
      <path d="M42 4h36v38h38v36H78v38H42V78H4V42h38z" fill="#ffffff" stroke="var(--navy)" stroke-width="3"/>
    </svg>
    <div class="brand"><span class="brand-mark"></span>Brightwell Harbor Systems</div>
  </section>

</main>
</body>
</html>
```